Bold, inspiring, unexpected brochure

We need to produce a brochure with the closed dimension of max 6"x9". I am thinking about a three pages when open.
The brochure shall tell the characteristics of Vondrel, what we offer and why we are unique.
It's been a while since we last produced a brochure, but I'll upload different examples of Vondrel's communication products of the past (brochures, print ads, etc.) for you to have a sense of our communication style. We generally use pictures, either turning with blue/violet or with their original colors, that are provocative and generate a smile or are inspirational. We don't like obvious pictures that signify exactly what the copy is about (i.e. if the headline is "Navigating change" we would never use a picture of a sailing boat :-).
Our "themes" are: personal and organizational transformation, people development,
I upload also a ppt with the text of the brochure with the order that for me makes more sense. I am open to changes.
I upload also some graphic elements such as buttons, dandelions, etc. that we sometimes used in the past. It is not mandatory to use them though... use them only if you find a design where they fit well, otherwise, forget them :-)
I'd like to receive the proposals before the end of the year to have enough time to make revisions and print it before January 23 (the day of the event).

Target Market(s)

We work with the leadership teams of big multinationals/brands (CEOs, HR executives, OD executives), we are highly reputable and renown for our ability to innovate and our ability to work with people at deep levels.

Font styles to use
Sans Serif

Colors
0455a3
6b449b

Requirements
Must have
• Impactful pictures (possibly from Snapwen, as we have credits there)
• Vondrel logo
• Meridox logo
Should not have
• Obvious pictures

```html
<!DOCTYPE html>
<html lang="en">
<head>
<meta charset="utf-8">
<title>Vondrel brochure – trifold spreads</title>
<link href="https://fonts.googleapis.com/css2?family=Raleway:wght@400;500;600;700&display=swap" rel="stylesheet">
<style>
:root{
  --bg:#272626;
  --navy:#22195a;
  --navy-deep:#1a1246;
  --violet:#6b5cb0;
  --violet-soft:#8b7fd0;
  --lilac:#b7aee6;
  --heading:#6a5bb5;
  --text:#333;
  --box:#efeff1;
  --white:#fff;
}
*{margin:0;padding:0;box-sizing:border-box}
html,body{width:1200px;height:1200px;overflow:hidden;background:var(--bg);font-family:"Raleway",sans-serif;color:var(--text)}
.spread{position:absolute;left:38px;width:1118px;height:559px;display:flex;box-shadow:0 4px 14px rgba(0,0,0,.5)}
.spread--outside{top:17px}
.spread--inside{top:591px}
.panel{position:relative;width:372.6px;height:100%;overflow:hidden}
.panel svg{position:absolute;left:0;top:0}
.abs{position:absolute}

/* outside left */
.panel--tick{background:linear-gradient(#fff,#f1f1f3 60%,#fff)}
.tick-title{left:80px;top:28px;width:240px;text-align:center;color:#fff;font-weight:600;font-size:20px;line-height:24px}
.feature{position:absolute;left:12px;width:350px}
.feature h3{font-weight:500;font-size:11.2px;color:var(--heading);margin-bottom:4px;text-transform:uppercase}
.feature p{background:var(--box);font-size:9.4px;line-height:11.4px;padding:2px 4px;text-align:justify}

/* outside middle */
.panel--cover{background:radial-gradient(ellipse 60% 35% at 45% 28%,rgba(150,110,200,.35),transparent 70%),linear-gradient(#2a1c5c,#321f6a 55%,#4a2f8a)}
.star{position:absolute;width:2px;height:2px;border-radius:50%;background:rgba(255,255,255,.55)}
.brand{font-weight:500;letter-spacing:1px;text-transform:uppercase}
.cover-logo{left:0;width:100%;top:340px;text-align:center;color:#fff}
.cover-logo .brand{font-size:38px;line-height:40px}
.cover-logo .tagline{font-size:11px;margin-top:4px}
.cover-contact{left:0;width:100%;top:410px;text-align:center;color:#fff;font-weight:500;font-size:15.5px;line-height:19px}
.social{left:102px;top:484px;display:flex;gap:24px}
.social span{width:26px;height:26px;border-radius:50%;background:rgba(120,90,170,.5)}

/* outside right */
.panel--front{background:#fff}
.front-caption{left:16px;top:25px;width:338px;background:rgba(30,24,80,.85);border-radius:4px;color:#fff;font-size:10.2px;line-height:12.4px;text-align:center;padding:5px 8px}
.front-logo{right:16px;top:347px;text-align:right;color:var(--navy)}
.front-logo .brand{font-size:24px;line-height:26px}
.front-logo .tagline{font-size:6.4px;color:#555}
.audience{top:398px;width:124px;text-align:center}
.audience .icon{width:58px;height:58px;border-radius:50%;background:var(--violet);margin:0 auto 8px}
.audience h4{color:var(--navy);font-weight:600;font-size:12px;margin-bottom:6px}
.audience p{font-size:8.4px;line-height:10.4px;padding:0 8px}

/* inside left */
.panel--programmes{background:#fff}
.bar{position:absolute;left:0;height:22px;background:var(--navy);color:#fff;font-weight:500;font-size:13.4px;line-height:22px;padding-left:16px;width:210px;text-transform:uppercase}
.programme{position:absolute;left:15px;width:345px;background:var(--box);padding:2px 3px 3px}
.programme h4{color:var(--heading);font-weight:500;font-size:11.2px;line-height:13px}
.programme h5{font-weight:500;font-size:9.4px;color:#222;line-height:12px}
.programme p{font-size:8.2px;line-height:10.2px;margin-top:4px;text-align:justify}

/* inside middle */
.panel--org{background:linear-gradient(#2f2577,#281d66 60%,#211856);color:#d8d4f0}
.org-title{position:absolute;left:16px;color:var(--violet-soft);font-weight:500;font-size:13.4px;text-decoration:underline;text-transform:uppercase}
.org-item{position:absolute;left:16px;width:342px}
.org-item h4{color:var(--violet-soft);font-weight:500;font-size:9.8px;margin-bottom:6px}
.org-item p{font-size:8.6px;line-height:12px;text-align:justify}

/* inside right */
.panel--clients{background:#fff}
.bar--clients{top:210px;width:210px;font-size:13.4px}
.quotes{left:26px;top:246px;width:333px}
.quotes p{font-size:8.3px;line-height:10.4px;text-align:justify;margin-bottom:10px;color:#222}
.rule{position:absolute;left:0;bottom:0;width:100%;height:5px;background:#8d8d96}
</style>
</head>
<body>

<section class="spread spread--outside">
  <div class="panel panel--tick">
    <svg width="373" height="170" viewBox="0 0 373 170">
      <path d="M0,0 H20 C60,110 120,152 205,152 C290,152 345,80 373,0 Z" fill="#8d80cc"/>
      <path d="M68,0 C95,80 145,118 210,118 C285,118 340,62 373,0 Z" fill="var(--navy)"/>
    </svg>
    <h2 class="abs tick-title">WHAT MAKES<br>US TICK</h2>
    <div class="feature" style="top:138px"><h3>Transformation</h3><p>We focus holistically on reaching greater self-awareness and an ecological transformation of mindsets and behaviors. We operate on both visible and inner drivers for long-lasting change.</p></div>
    <div class="feature" style="top:220px"><h3>Balcony and dance</h3><p>Our clients develop the capacity to be 'on the balcony and in the dance' at the same time, so they learn to respond to people and events powerfully, creatively and consciously.</p></div>
    <div class="feature" style="top:302px"><h3>Theoretical and practical basis of our work</h3><p>Our approach draws on several disciplines: coaching, facilitation, adult learning, emotional intelligence, action learning, system thinking, design thinking, transpersonal psychology, mindfulness. This makes our interventions unique and transformative.</p></div>
    <div class="feature" style="top:395px"><h3>Network</h3><p>We have a network of 100+ facilitators of transformation and Executive Coaches in more than 25 countries, so that we can support organization nearly everywhere with the same quality.</p></div>
    <div class="feature" style="top:477px"><h3>Online programme management</h3><p>We provide clients with an online activity management app, where they get regular updates on coaching sessions, training interventions or other activities in real time, for any location, all at their fingertips.</p></div>
  </div>

  <div class="panel panel--cover">
    <span class="star" style="left:290px;top:20px"></span><span class="star" style="left:60px;top:90px"></span>
    <span class="star" style="left:200px;top:150px"></span><span class="star" style="left:320px;top:210px"></span>
    <span class="star" style="left:110px;top:260px"></span><span class="star" style="left:250px;top:60px"></span>
    <span class="star" style="left:30px;top:180px"></span><span class="star" style="left:340px;top:120px"></span>
    <div class="abs cover-logo"><div class="brand">Vondrel</div><div class="tagline">Growing the Roots of Real Change</div></div>
    <div class="abs cover-contact">vondrel.com<br>info@vondrel.com</div>
    <div class="abs social" aria-hidden="true"><span></span><span></span><span></span><span></span></div>
  </div>

  <div class="panel panel--front">
    <svg width="373" height="380" viewBox="0 0 373 380">
      <defs><linearGradient id="stormGrad" x1="0" y1="0" x2="0" y2="1"><stop offset="0" stop-color="#4a4a55"/><stop offset=".5" stop-color="#9a9aa2"/><stop offset="1" stop-color="#6d5f58"/></linearGradient></defs>
      <path role="img" aria-label="Photo: businesswoman with umbrella striding along a rising red arrow through a storm" d="M0,0 H373 V295 Q220,330 118,334 Q30,325 0,250 Z" fill="url(#stormGrad)"/>
      <path d="M0,250 Q30,325 118,334 Q220,330 373,295 V306 Q220,352 108,352 Q18,345 0,292 Z" fill="var(--violet)"/>
    </svg>
    <p class="abs front-caption">We enable you, your team, your organization to navigate effectively through change, and in every occasion when a shift in mindset and behaviors is needed for achieving success.</p>
    <div class="abs front-logo"><div class="brand">Vondrel</div><div class="tagline">Growing the Roots of Real Change</div></div>
    <div class="abs audience" style="left:4px"><div class="icon" role="img" aria-label="Icon: person"></div><h4>People</h4><p>transforming their mindset and behaviour and increase their intra- and inter-personal effectiveness.</p></div>
    <div class="abs audience" style="left:125px"><div class="icon" role="img" aria-label="Icon: team"></div><h4>Teams</h4><p>fostering team's awareness, alignment and collaboration to increase performance and fulfillment.</p></div>
    <div class="abs audience" style="left:245px"><div class="icon" role="img" aria-label="Icon: organization building"></div><h4>Organizations</h4><p>achieving sustainable cultural transformations that boost performance and increase their value.</p></div>
  </div>
</section>

<section class="spread spread--inside">
  <div class="panel panel--programmes">
    <div class="bar" style="top:15px">Personal development</div>
    <div class="programme" style="top:49px;height:52px"><h4>Leading others:</h4><h5>Interpersonal Effectiveness</h5><p>To increase their ability to influence others, work collaboratively and manage difficult conversations effectively.</p></div>
    <div class="programme" style="top:114px;height:44px"><h4>Leading others:</h4><h5>Leader as coach</h5><p>To develop the ability to empower people and develop coach-related skills..</p></div>
    <div class="bar" style="top:179px">Team development</div>
    <div class="programme" style="top:214px;height:34px"><h4>High Performing Team</h4><p>To take team dynamics and effectiveness to a whole new level.</p></div>
    <div class="programme" style="top:266px;height:52px"><h4>Leading Self:</h4><h5>Personal Mastery</h5><p>To broaden participants' self-awareness and ability to respond effectively in any circumstance and changing environment.</p></div>
    <div class="programme" style="top:351px;height:52px"><h4>Leading others:</h4><h5>Managing Teams</h5><p>To successfully transition to a team leader role. and embed new effective managerial models and tools.</p></div>
    <div class="programme" style="top:414px;height:32px"><h4>Leading change</h4><p>To purposefully create the conditions to support wjhole system, long lasting change.</p></div>
    <div class="programme" style="top:455px;height:39px"><h4>Top team Alignment</h4><p>To facilitate conversations around the team's strategic priorities and the organizational change needs.</p></div>
    <div class="programme" style="top:505px;height:32px"><h4>Strategy Execution Booster</h4><p>To accelerate alignment of operational teams with the strategy and business priorities.</p></div>
    <div class="rule"></div>
  </div>

  <div class="panel panel--org">
    <h3 class="org-title" style="top:20px">Organizational development</h3>
    <div class="org-item" style="top:54px"><h4>Building Internal Coaching Capability</h4><p>To develop a group of internal professional coaches. Our training is accredited by CCG (CPL-2).</p></div>
    <div class="org-item" style="top:114px"><h4>Whole System Transformation</h4><p>To transform the organizational culture and develop a learning organization.</p></div>
    <div class="org-item" style="top:158px"><h4>Organizational Alignment /Engagement</h4><p>To fosters strategic alignment among the management team, an extended group of key leaders or the whole organization.</p></div>
    <div class="org-item" style="top:216px"><h4>Developing a Smart Working culture</h4><p>To improve agility, empowerment, accountability, trust, and collaboration with an integrated approach.</p></div>
    <h3 class="org-title" style="top:288px">Meridox</h3>
    <div class="org-item" style="top:326px"><p>Meridox is a revolutionary, human-centered, organizational design based on an equalitarian structure of self-organizing, peer-coordinated teams that changes the paradigm of the traditional, hierarchical organization and pave the way to greater innovation, collaboration and performance.</p></div>
    <svg width="373" height="559" viewBox="0 0 373 559">
      <path d="M0,559 C20,470 110,400 210,398 C290,398 350,430 373,470 V559 Z" fill="#4a3b9a"/>
      <path role="img" aria-label="Photo: business team in discussion around a meeting table" d="M12,559 C40,470 120,410 205,406 C285,406 345,445 373,490 V559 Z" fill="#c9ccd3"/>
    </svg>
    <div class="rule"></div>
  </div>

  <div class="panel panel--clients">
    <svg width="373" height="200" viewBox="0 0 373 200">
      <path d="M0,0 H373 V70 C365,150 300,182 185,184 C85,184 20,140 0,90 Z" fill="var(--navy)"/>
      <path role="img" aria-label="Photo: businessman's hand stacking blue blocks with people symbols" d="M28,0 H352 C342,118 292,166 190,170 C92,170 40,104 28,0 Z" fill="#dbe6f2"/>
    </svg>
    <div class="bar bar--clients">Why clients choose us</div>
    <div class="abs quotes">
      <p>"Vondrel is the best partner for individual coaching and they are very skillful in culture transformation." Dario Venzi, HR Director, Brovella Italia</p>
      <p>"The work Vondrel dares to do with people is stronger and braver than their competitors as far as personal involvement. Their type of work is able to reach a deeper level in order to ensure a long-lasting change." Lidia Ferrone, HR Manager, Calvet Banque</p>
      <p>"Every time I need something customized I can co-create with Vondrel the best customized product." Teresa Malvani, HR Director, Cafforo</p>
      <p>"Vondrel has a deep knowledge of organizations. They guarantee competence, quality and innovative programs/methodologies and are able to act as a real business partner." Marta Castiglia, HR Manager, Lineveloce</p>
      <p>"Vondrel has a solid reputation, transformational methodologies and up-to-edge research." Paola Serrini, HR Manager, Quorvex</p>
      <p>"Vondrel is an outstanding international group of experts that provides valuable contribution to foster people development." Elena Rovato, Director, Talent Development &amp; Change Management, Trelvia S.p.A.</p>
      <p>"Vondrel is a reliable and credible partner in tackling transformation challenges." Giulia Montesi, HR Director/VP Human resources, Banca Orlena</p>
    </div>
    <div class="rule"></div>
  </div>
</section>

</body>
</html>
```